hello! I need a very simple modern business card for a new venture called The Quiet Harbour Asia. It's the very first Tech-Free retreat in Asia!

The concept is very unique. Basically a group of 12-15 people would go on a 3 to 4 days retreat where no phone or internet is allowed. The first retreat will take place in a beautiful villa in Bali by the sea. It will include yoga, meditation, art & writing workshops, swimming, hiking, cooking, healthy vegetarian meals, etc.

Reason: Thanks for your submissions. I still haven't found exactly what I'm after but the designs that haven't be eliminated are getting close.. Please keep in mind that it should be a simple, modern and upmarket business card. Thanks

Target Market(s)

Both men and women who would like to disconnect from life, computer and phone for 3/4 days. They can be either local or expats but based in Asia (Singapore, Hong Kong).
Client will have to pay for their own flight and then the price is around US$600 for a 3-day retreat including everything (accommodation, food, activities). It means clients already have a good income. They are usually working in marketing, advertising, digital media, public relations.

Industry/Entity Type

Internet

Font styles to use
Other font styles liked:
• anything modern you like

Colors
acd036
9bcb3c
f37022
f68d4d
1b1b1b
333333
acd037

Requirements
Must have
• Name: Rel Vontaine
Position: #screenwanderer
Company: The Quiet Harbour Asia (asia should be smaller than the rest)
- Email button - quietharbourasia@mailnest.example
- Facepage button - www.facepage.example/quietharbourasia
- Ticketloom button - www.quietharbourasia.ticketloom.example
Nice to have
• You can use my logo attached but it's something I designed quickly on Power Point so it would be nice to include your own version.
Should not have
• anything tacky or girly or childish. thanks

```html
<!DOCTYPE html>
<html lang="en">
<head>
<meta charset="utf-8">
<title>The Quiet Harbour Asia – Business Card</title>
<link rel="stylesheet" href="https://fonts.googleapis.com/css2?family=Questrial&display=swap">
<style>
  :root {
    --lime: #acd036;
    --lime-deep: #9bcb3c;
    --orange: #f37022;
    --charcoal: #333333;
    --ink: #1b1b1b;
    --backdrop-center: #ffffff;
    --backdrop-edge: #e9e9e9;
  }
  * { margin: 0; padding: 0; box-sizing: border-box; }
  html, body {
    width: 1200px; height: 1000px; overflow: hidden;
  }
  body {
    position: relative;
    background: radial-gradient(ellipse at center, var(--backdrop-center) 45%, var(--backdrop-edge) 100%);
    font-family: "Questrial", "Helvetica Neue", Arial, sans-serif;
  }
  .card {
    position: absolute;
    left: 199px;
    width: 800px;
    overflow: hidden;
  }

  /* Front */
  .card--front {
    top: 20px;
    height: 458px;
    background: var(--orange);
  }
  .brand {
    position: absolute;
    left: 116px;
    top: 160px;
    display: flex;
    align-items: center;
    gap: 14px;
  }
  .brand__dot {
    width: 136px; height: 136px;
    border-radius: 50%;
    background: var(--lime);
  }
  .brand__name {
    color: var(--lime);
    font-size: 36px;
    letter-spacing: 1px;
    white-space: nowrap;
  }
  .brand__region { font-size: 23px; }
  .card__footer {
    position: absolute;
    left: 0; bottom: 0;
    width: 100%; height: 37px;
    background: var(--charcoal);
    color: var(--orange);
    font-size: 15px;
    letter-spacing: 0.5px;
    text-align: center;
    line-height: 37px;
  }

  /* Back */
  .card--back {
    top: 522px;
    height: 457px;
    background: var(--charcoal);
  }
  .person {
    position: absolute;
    left: 26px;
    top: 168px;
    color: var(--lime);
  }
  .person__name {
    font-size: 52px;
    letter-spacing: 2px;
    line-height: 1.1;
    white-space: nowrap;
  }
  .person__role {
    font-size: 39px;
    letter-spacing: 0.5px;
    line-height: 1.15;
    white-space: nowrap;
  }
  .divider {
    position: absolute;
    left: 397px;
    top: 62px;
    width: 4px;
    height: 330px;
    background: linear-gradient(to bottom, rgba(27,27,27,0), var(--ink) 30%, var(--ink) 70%, rgba(27,27,27,0));
  }
  .contacts {
    position: absolute;
    left: 422px;
    top: 164px;
    list-style: none;
  }
  .contact {
    display: flex;
    align-items: center;
    gap: 13px;
    height: 32px;
    margin-bottom: 15.5px;
    color: var(--lime);
    font-size: 15px;
    letter-spacing: 0.4px;
    white-space: nowrap;
  }
  .contact__icon {
    width: 31px; height: 31px;
    flex: none;
    display: block;
  }
  .contact__badge {
    width: 31px; height: 31px;
    flex: none;
    border-radius: 4px;
    background: var(--lime-deep);
  }
</style>
</head>
<body>
  <section class="card card--front" aria-label="Business card front">
    <div class="brand">
      <span class="brand__dot" aria-hidden="true"></span>
      <span class="brand__name">The Quiet Harbour <span class="brand__region">Asia</span></span>
    </div>
    <div class="card__footer">www.quietharbourasia.example</div>
  </section>

  <section class="card card--back" aria-label="Business card back">
    <div class="person">
      <p class="person__name">Rel Vontaine</p>
      <p class="person__role">#screenwanderer</p>
    </div>
    <div class="divider" aria-hidden="true"></div>
    <ul class="contacts">
      <li class="contact">
        <svg class="contact__icon" viewBox="0 0 32 32" aria-hidden="true">
          <rect x="1" y="6" width="30" height="20" fill="var(--lime)"/>
          <path d="M1 6 L16 18 L31 6" fill="none" stroke="var(--charcoal)" stroke-width="2.5"/>
          <path d="M1 26 L12 15 M31 26 L20 15" fill="none" stroke="var(--charcoal)" stroke-width="2.5"/>
        </svg>
        <span>quietharbourasia@mailnest.example</span>
      </li>
      <li class="contact">
        <span class="contact__badge" aria-hidden="true"></span>
        <span>www.facepage.example/quietharbourasia</span>
      </li>
      <li class="contact">
        <span class="contact__badge" aria-hidden="true"></span>
        <span>www.quietharbourasia.ticketloom.example</span>
      </li>
    </ul>
  </section>
</body>
</html>
```